Sandwich Board and Poster design promoting a medical aesthetic clinic

I am looking for a clean, modern and relaxing design promoting a medical physician-led aesthetic clinic.
Services offered are neuromodulator treatment (Quelvo) and Dermal Fillers.
Logo must be included.
Use the tag line "Refresh your look, revive your spirit."
Address is 204-205 27361 92 Ave, Surrey, V7K 2M4
604-555-0148
email - info@lumawellpine.ca
www.lumawellpine.ca

```html
<!DOCTYPE html>
<html lang="en">
<head>
<meta charset="utf-8">
<title>Lumawell Pine – Poster</title>
<link rel="stylesheet" href="https://fonts.googleapis.com/css2?family=Montserrat:wght@400;500;600;700&family=Poiret+One&family=Poppins:wght@400;500;700&display=swap">
<style>
  :root{
    --stage:#cbcbcb;
    --navy:#1b2f52;
    --navy-soft:#213a63;
    --gold:#e0b52a;
    --gold-deep:#b79a3a;
    --white:#ffffff;
    --ink:#1a1a1a;
    --sky:#a6def0;
    --skin:#d7a486;
  }
  *{margin:0;padding:0;box-sizing:border-box}
  html,body{width:1200px;height:1200px;overflow:hidden;background:var(--stage)}
  .poster{position:absolute;left:233px;top:50px;width:733px;height:1100px;background:var(--navy);overflow:hidden;font-family:"Montserrat",sans-serif;color:var(--white)}
  .poster-shapes{position:absolute;inset:0}
  .hero-photo{position:absolute;left:0;top:0;width:733px;height:430px;background:linear-gradient(180deg,var(--sky) 0%,#e9f3f7 40%,var(--skin) 75%,#6b4a33 100%)}
  .inset-photo{position:absolute;left:453px;top:251px;width:204px;height:204px;border-radius:50%;border:6px solid var(--gold-deep);background:radial-gradient(circle at 60% 40%,#f0c9b5 0%,#e3ac95 45%,#dfe4ea 80%)}
  .brand{position:absolute;left:0;width:733px;top:448px;text-align:center}
  .brand-mark{display:block;margin:0 auto 8px;width:16px;height:16px;border-radius:50%;background:var(--gold)}
  .brand-name{font-size:20px;letter-spacing:6px;font-weight:500;color:var(--white)}
  .headline{position:absolute;left:0;width:733px;top:560px;text-align:center}
  .headline-lead{font-weight:600;font-size:37px;letter-spacing:.5px;line-height:1}
  .headline-accent{font-family:"Poiret One",sans-serif;color:var(--gold);font-size:64px;line-height:62px;margin-top:8px;font-weight:400}
  .divider{position:absolute;left:127px;top:753px;width:478px;height:1px;background:rgba(255,255,255,.45)}
  .divider-pill{position:absolute;left:323px;top:750px;width:87px;height:7px;border-radius:4px;background:var(--gold)}
  .services-title{position:absolute;left:0;width:733px;top:782px;text-align:center;font-family:"Poppins",sans-serif;font-size:24px;letter-spacing:3px;font-weight:400}
  .services-title strong{font-weight:700}
  .service{position:absolute;display:flex;align-items:center;gap:12px;font-family:"Poppins",sans-serif;font-size:19.5px;line-height:1.2;font-weight:500}
  .service-icon{width:51px;height:51px;border-radius:50%;background:var(--gold);flex:none}
  .service--neuro{left:93px;top:825px}
  .service--filler{left:401px;top:825px}
  .phone-pill{position:absolute;left:177px;top:912px;width:378px;height:44px;border-radius:22px;background:var(--gold);display:flex;align-items:center}
  .phone-badge{width:34px;height:34px;border-radius:50%;background:var(--white);margin-left:5px;display:flex;align-items:center;justify-content:center}
  .phone-number{font-family:"Poppins",sans-serif;font-weight:700;color:var(--ink);font-size:30px;letter-spacing:6px;margin-left:20px}
  .contact-line{position:absolute;left:0;width:733px;top:985px;display:flex;justify-content:center;gap:20px;font-family:"Poppins",sans-serif;font-size:17.5px;color:var(--ink)}
  .contact-item{display:flex;align-items:center;gap:8px}
  .website{position:absolute;left:0;width:733px;top:1018px;text-align:center;font-family:"Poppins",sans-serif;font-weight:700;font-size:25px;letter-spacing:3.5px;color:var(--ink)}
  .website-domain{color:var(--navy)}
</style>
</head>
<body>
<div class="poster">
  <div class="hero-photo" role="img" aria-label="Photo of a practitioner in gloves giving a cosmetic injection to a relaxed client lying on a towel"></div>
  <svg class="poster-shapes" width="733" height="1100" viewBox="0 0 733 1100">
    <defs>
      <linearGradient id="navyFade" x1="0" y1="0" x2="1" y2="1">
        <stop offset="0" stop-color="#1f3a66"/>
        <stop offset="1" stop-color="#18294a"/>
      </linearGradient>
    </defs>
    <path d="M0 300 C120 400 260 440 440 360 C560 310 660 340 733 372 L733 1100 L0 1100 Z" fill="var(--gold)"/>
    <path d="M0 325 C120 410 260 420 440 375 C560 340 660 350 733 380 L733 1100 L0 1100 Z" fill="url(#navyFade)"/>
    <path d="M0 962 Q366 900 733 962 L733 1100 L0 1100 Z" fill="var(--white)"/>
  </svg>
  <div class="inset-photo" role="img" aria-label="Close-up photo of a lip filler treatment with a gloved hand"></div>

  <div class="brand">
    <span class="brand-mark"></span>
    <div class="brand-name">LUMAWELL PINE</div>
  </div>

  <div class="headline">
    <div class="headline-lead">REFRESH YOUR LOOK,</div>
    <div class="headline-accent">REVIVE<br>YOUR SPIRIT</div>
  </div>

  <div class="divider"></div>
  <div class="divider-pill"></div>

  <div class="services-title"><strong>SERVICES</strong> WE OFFER</div>

  <div class="service service--neuro">
    <svg class="service-icon" viewBox="0 0 51 51"><circle cx="25.5" cy="25.5" r="25.5" fill="var(--gold)"/><g stroke="var(--navy)" stroke-width="1.6" fill="none"><circle cx="20" cy="22" r="4"/><circle cx="31" cy="28" r="4"/><path d="M14 16l6 6 11 6 6-6M20 22l-4 10M31 28l2 9"/></g></svg>
    <span>Neuromodulator<br>treatment (Quelvo)</span>
  </div>
  <div class="service service--filler">
    <svg class="service-icon" viewBox="0 0 51 51"><circle cx="25.5" cy="25.5" r="25.5" fill="var(--gold)"/><g stroke="var(--navy)" stroke-width="1.6" fill="none"><path d="M14 26q11-9 23 0q-11 9-23 0z"/><path d="M14 26h23M22 17v-5M29 17v-5M20 14l2-2 2 2M27 14l2-2 2 2"/></g></svg>
    <span>Dermal Fillers</span>
  </div>

  <div class="phone-pill">
    <div class="phone-badge">
      <svg width="20" height="20" viewBox="0 0 24 24"><path d="M6.6 10.8a15 15 0 0 0 6.6 6.6l2.2-2.2a1 1 0 0 1 1-.25 11.4 11.4 0 0 0 3.6.57 1 1 0 0 1 1 1V20a1 1 0 0 1-1 1A17 17 0 0 1 3 4a1 1 0 0 1 1-1h3.5a1 1 0 0 1 1 1c0 1.25.2 2.45.57 3.6a1 1 0 0 1-.25 1z" fill="var(--ink)"/></svg>
    </div>
    <span class="phone-number">604-555-0148</span>
  </div>

  <div class="contact-line">
    <span class="contact-item">
      <svg width="22" height="16" viewBox="0 0 22 16"><rect x="1" y="1" width="20" height="14" fill="none" stroke="var(--navy)" stroke-width="2"/><path d="M1 1l10 8 10-8M1 15l7-7M21 15l-7-7" fill="none" stroke="var(--navy)" stroke-width="2"/></svg>
      info@lumawellpine.ca
    </span>
    <span class="contact-item">
      <svg width="16" height="20" viewBox="0 0 16 20"><path d="M8 0a8 8 0 0 0-8 8c0 6 8 12 8 12s8-6 8-12a8 8 0 0 0-8-8zm0 11a3 3 0 1 1 0-6 3 3 0 0 1 0 6z" fill="var(--navy)"/></svg>
      204-205 27361 92 Ave, Surrey, V7K 2M4
    </span>
  </div>

  <div class="website">www.<span class="website-domain">lumawellpine</span>.ca</div>
</div>
</body>
</html>
```